pop up booking component and calendar re-design

we have a calander view where a parent cant reserve a day
you can click on please redesign the calander / voucher and pop up.

the dropdowns in pop up can be buttons
the dots on the calander indicate if there is space or not

when booking a day you can select a voucher

we used KIVO as inspiration, you are welcome to look at it as well.. screenshots attached

please ask questions if you have any

```html
<!DOCTYPE html>
<html lang="en">
<head>
<meta charset="utf-8">
<title>Choose Dates – booking pop-up</title>
<link rel="stylesheet" href="https://fonts.googleapis.com/css2?family=Open+Sans:wght@400;600;700&display=swap">
<style>
  :root{
    --green:#4fae5a;
    --green-soft:#6fb77a;
    --yellow:#f6d06e;
    --coral:#ec7563;
    --ink:#1e1e1e;
    --muted:#9a9a9a;
    --line:#e4e4e4;
    --band:#f5f5f5;
    --page:#eef0ee;
    --white:#ffffff;
  }
  *{box-sizing:border-box;margin:0;padding:0}
  html,body{width:1200px;height:996px;overflow:hidden}
  body{background:var(--page);font-family:"Open Sans",sans-serif;color:var(--ink);position:relative}

  .screen{position:absolute;top:54px;width:410px;height:886px;background:var(--white);border-radius:28px;overflow:hidden;box-shadow:0 6px 24px rgba(0,0,0,.12)}
  .screen--book{left:122px}
  .screen--voucher{left:668px}

  .header{position:absolute;left:0;top:0;width:100%;height:97px;background:var(--green)}
  .header__title{position:absolute;left:28px;top:40px;color:var(--white);font-size:20px;font-weight:400}
  .header__close{position:absolute;left:353px;top:44px;width:18px;height:18px}

  .price-row{position:absolute;left:0;top:97px;width:100%;height:46px;border-bottom:1px solid var(--line)}
  .price-row__text{position:absolute;left:28px;top:14px;font-size:13px;color:#777}
  .price-row__text span{margin-right:14px}
  .price-row__info{position:absolute;left:351px;top:11px;width:22px;height:22px}

  .month{position:absolute;left:28px;font-size:13.5px;font-weight:700}
  .month--march{top:170px}
  .month--april{top:527px}

  .weekdays{position:absolute;left:0;top:210px;width:100%;height:46px;background:var(--band);display:grid;grid-template-columns:repeat(7,52px);padding-left:22px;align-items:center}
  .weekdays span{text-align:center;font-size:13px;color:var(--muted)}

  .band{position:absolute;left:0;width:100%;height:40px;background:var(--band)}

  .days{position:absolute;left:22px;top:262px;display:grid;grid-template-columns:repeat(7,52px);grid-auto-rows:46.5px}
  .day{position:relative;display:flex;align-items:center;justify-content:center;font-size:13.5px;font-weight:600}
  .day--out{color:#a8a8a8;font-weight:400}
  .day--today,.day--selected{color:var(--white)}
  .day--today::before,.day--selected::before{content:"";position:absolute;width:40px;height:40px;border-radius:50%;z-index:-1}
  .day--today::before{background:var(--yellow)}
  .day--selected::before{background:var(--green)}
  .day{z-index:1}
  .day--full::after,.day--free::after{content:"";position:absolute;top:8px;right:8px;width:4px;height:4px;border-radius:50%}
  .day--full::after{background:var(--coral)}
  .day--free::after{background:var(--green)}

  .calendar-card{position:absolute;left:0;top:0;width:100%;height:571px;border-radius:0 0 14px 14px;box-shadow:0 6px 10px rgba(0,0,0,.08)}
  .divider-month{position:absolute;left:0;top:504px;width:100%;height:1px;background:var(--line)}

  .tabs{position:absolute;left:18px;top:602px;width:374px;height:82px;border-bottom:1px solid var(--line)}
  .tab{position:absolute;top:0;width:120px;margin-left:-60px;text-align:center}
  .tab--book{left:48px}
  .tab--vouchers{left:188px}
  .tab--options{left:321px}
  .tab__icon{height:30px;display:flex;align-items:center;justify-content:center;position:relative}
  .tab__label{display:inline-block;font-size:14.5px;color:var(--muted);margin-top:5px;padding-bottom:2px}
  .tab--active .tab__label{border-bottom:2px solid var(--green)}
  .date-chip{width:46px;height:28px;color:var(--white);font-size:13px;font-weight:600;display:flex;align-items:center;justify-content:center}
  .date-chip--on{background:var(--green)}
  .date-chip--off{background:#b3b3b3}
  .badge{position:absolute;left:75px;top:-12px;width:10px;height:10px;border-radius:50%;background:var(--green)}
  .dots{display:flex;gap:10px}
  .dots i{width:7px;height:7px;border-radius:50%;background:#a8a8a8}
  .tab-sep{position:absolute;top:20px;width:1px;height:46px;background:var(--line)}

  .choices{position:absolute;left:18px;top:684px;width:374px;height:72px;border-bottom:1px solid var(--line)}
  .pill{position:absolute;top:19px;width:82px;height:33px;border-radius:12px;background:var(--green-soft);color:var(--white);font-size:10.5px;display:flex;align-items:center;justify-content:center;box-shadow:0 3px 6px rgba(0,0,0,.15)}
  .pill--locations{left:10px}
  .pill--time{left:283px;top:18px}
  .choices__text{position:absolute;left:116px;width:140px;top:24px;text-align:center;font-size:15px;color:var(--muted)}
  .amount{position:absolute;top:12px;width:92px;height:46px;color:var(--white);font-size:17px;font-weight:700;display:flex;align-items:center;justify-content:center;border-radius:3px;box-shadow:0 4px 8px rgba(0,0,0,.15)}
  .amount--10{left:28px;background:var(--green)}
  .amount--15{left:142px;background:var(--yellow)}
  .amount--20{left:255px;background:var(--coral)}

  .toggle-row{position:absolute;left:0;top:766px;width:100%;height:22px}
  .toggle{position:absolute;left:166px;top:4px;width:29px;height:15px;border:1.5px solid #cfcfcf;border-radius:8px}
  .toggle::before{content:"";position:absolute;left:0;top:0;width:12px;height:12px;border-radius:50%;background:var(--green)}
  .toggle-row__label{position:absolute;left:212px;top:0;font-size:15.5px;font-weight:600;color:#8a8a8a}

  .pay{position:absolute;left:18px;top:802px;width:374px;height:57px;background:var(--green);border-radius:8px;color:var(--white);font-size:16.5px;font-weight:600;display:flex;align-items:center;justify-content:center;box-shadow:0 6px 10px rgba(79,174,90,.3)}
  .pay span{margin-right:22px}
</style>
</head>
<body>

<!-- Screen: booking a day -->
<section class="screen screen--book">
  <div class="calendar-card"></div>
  <header class="header">
    <h1 class="header__title">Choose Dates</h1>
    <svg class="header__close" viewBox="0 0 18 18"><path d="M2 2L16 16M16 2L2 16" stroke="#fff" stroke-width="2"/></svg>
  </header>
  <div class="price-row">
    <p class="price-row__text"><span>$</span>98,23 USD</p>
    <svg class="price-row__info" viewBox="0 0 22 22"><circle cx="11" cy="11" r="10" fill="none" stroke="#8a8a8a" stroke-width="1.3"/><circle cx="11" cy="6.5" r="1.1" fill="#8a8a8a"/><path d="M11 9.5V16" stroke="#8a8a8a" stroke-width="1.5"/></svg>
  </div>
  <h2 class="month month--march">March 2019</h2>
  <div class="weekdays"><span>Mo</span><span>To</span><span>We</span><span>Th</span><span>Fr</span><span>Sa</span><span>Su</span></div>
  <div class="band" style="top:355px"></div>
  <div class="band" style="top:402px"></div>
  <div class="days">
    <span class="day day--out">25</span><span class="day day--out">26</span><span class="day day--out">27</span><span class="day day--out">28</span><span class="day day--full">1</span><span class="day day--full">2</span><span class="day day--full">3</span>
    <span class="day">4</span><span class="day">5</span><span class="day day--full">6</span><span class="day day--full">7</span><span class="day day--full">8</span><span class="day">9</span><span class="day">10</span>
    <span class="day">11</span><span class="day">12</span><span class="day day--today">13</span><span class="day">14</span><span class="day">15</span><span class="day">16</span><span class="day">17</span>
    <span class="day">18</span><span class="day">19</span><span class="day">20</span><span class="day">21</span><span class="day">22</span><span class="day day--selected">23</span><span class="day day--free">24</span>
    <span class="day">25</span><span class="day">26</span><span class="day">27</span><span class="day day--free">28</span><span class="day">29</span><span class="day">30</span><span class="day">31</span>
  </div>
  <div class="divider-month"></div>
  <h2 class="month month--april">April 2019</h2>

  <nav class="tabs">
    <div class="tab tab--book tab--active"><div class="tab__icon"><div class="date-chip date-chip--on">24</div></div><span class="tab__label">Book Day</span></div>
    <div class="tab-sep" style="left:116px"></div>
    <div class="tab tab--vouchers"><div class="tab__icon">
      <svg width="44" height="30" viewBox="0 0 44 30"><rect x="1" y="1" width="42" height="28" fill="none" stroke="#9a9a9a" stroke-width="1.5"/><path d="M8 3V27" stroke="#9a9a9a" stroke-dasharray="3 2"/><text x="12" y="13" font-size="10" fill="#9a9a9a" font-family="Open Sans,sans-serif">%</text><path d="M24 8H38M24 13H38M24 18H38M13 23H38" stroke="#9a9a9a" stroke-width="1.3"/></svg>
      <i class="badge"></i></div><span class="tab__label">Vouchers</span></div>
    <div class="tab-sep" style="left:252px"></div>
    <div class="tab tab--options"><div class="tab__icon"><div class="dots"><i></i><i></i><i></i></div></div><span class="tab__label">Options</span></div>
  </nav>

  <div class="choices">
    <div class="pill pill--locations">Locations</div>
    <div class="tab-sep" style="left:116px;top:14px"></div>
    <p class="choices__text">Groups</p>
    <div class="tab-sep" style="left:252px;top:14px"></div>
    <div class="pill pill--time">Time</div>
  </div>

  <div class="toggle-row"><span class="toggle"></span><span class="toggle-row__label">BSO</span></div>
  <div class="pay"><span>$</span>98,23 USD</div>
</section>

<!-- Screen: choosing a voucher -->
<section class="screen screen--voucher">
  <div class="calendar-card"></div>
  <header class="header">
    <h1 class="header__title">Choose Dates</h1>
    <svg class="header__close" viewBox="0 0 18 18"><path d="M2 2L16 16M16 2L2 16" stroke="#fff" stroke-width="2"/></svg>
  </header>
  <div class="price-row">
    <p class="price-row__text"><span>$</span>98,23 USD</p>
    <svg class="price-row__info" viewBox="0 0 22 22"><circle cx="11" cy="11" r="10" fill="none" stroke="#8a8a8a" stroke-width="1.3"/><circle cx="11" cy="6.5" r="1.1" fill="#8a8a8a"/><path d="M11 9.5V16" stroke="#8a8a8a" stroke-width="1.5"/></svg>
  </div>
  <h2 class="month month--march">March 2019</h2>
  <div class="weekdays"><span>Mo</span><span>To</span><span>We</span><span>Th</span><span>Fr</span><span>Sa</span><span>Su</span></div>
  <div class="band" style="top:355px"></div>
  <div class="band" style="top:402px"></div>
  <div class="days">
    <span class="day day--out">25</span><span class="day day--out">26</span><span class="day day--out">27</span><span class="day day--out">28</span><span class="day day--full">1</span><span class="day day--full">2</span><span class="day day--full">3</span>
    <span class="day">4</span><span class="day">5</span><span class="day day--full">6</span><span class="day day--full">7</span><span class="day day--full">8</span><span class="day">9</span><span class="day">10</span>
    <span class="day">11</span><span class="day">12</span><span class="day day--today">13</span><span class="day">14</span><span class="day">15</span><span class="day">16</span><span class="day">17</span>
    <span class="day">18</span><span class="day">19</span><span class="day">20</span><span class="day">21</span><span class="day">22</span><span class="day day--selected">23</span><span class="day day--free">24</span>
    <span class="day">25</span><span class="day">26</span><span class="day">27</span><span class="day day--free">28</span><span class="day">29</span><span class="day">30</span><span class="day">31</span>
  </div>
  <div class="divider-month"></div>
  <h2 class="month month--april">April 2019</h2>

  <nav class="tabs">
    <div class="tab tab--book"><div class="tab__icon"><div class="date-chip date-chip--off">24</div></div><span class="tab__label">Book Day</span></div>
    <div class="tab-sep" style="left:116px"></div>
    <div class="tab tab--vouchers tab--active"><div class="tab__icon">
      <svg width="44" height="30" viewBox="0 0 44 30"><rect x="1" y="1" width="42" height="28" fill="none" stroke="#4fae5a" stroke-width="1.5"/><path d="M8 3V27" stroke="#4fae5a" stroke-dasharray="3 2"/><text x="12" y="13" font-size="10" fill="#4fae5a" font-family="Open Sans,sans-serif">%</text><path d="M24 8H38M24 13H38M24 18H38M13 23H38" stroke="#4fae5a" stroke-width="1.3"/></svg>
      <i class="badge"></i></div><span class="tab__label">Vouchers</span></div>
    <div class="tab-sep" style="left:252px"></div>
    <div class="tab tab--options"><div class="tab__icon"><div class="dots"><i></i><i></i><i></i></div></div><span class="tab__label">Options</span></div>
  </nav>

  <div class="choices">
    <div class="amount amount--10">$ 10</div>
    <div class="amount amount--15">$ 15</div>
    <div class="amount amount--20">$ 20</div>
  </div>

  <div class="toggle-row"><span class="toggle"></span><span class="toggle-row__label">Voucher</span></div>
  <div class="pay"><span>$</span>88,23 USD</div>
</section>

</body>
</html>
```